Shiftwell Hub

Our product is a subscription-based website for doctors and medical practices. It allows contract-based doctors (locums) to book jobs with medical practices and to organise their own finances (invoicing, pension, etc). Also, it allows medical practices to post jobs, and book locums.

We need a website design that looks clean and professional. It should look easy-to-use and friendly, which will encourage users to sign up as they'll hopefully think using the system will also be simple and friendly.

As well as the homepage, we need a design for the logged-in view. This is very different to the website but equally important. It needs to be very functional. Much more like an application and less like a website.

PLEASE SUBMIT BOTH WEBSITE HOMEPAGE DESIGN AND APPLICATION DASHBOARD DESIGN.

The application is built and we already have a user interface (linked below) so we're not looking for a designer to decide what is on these pages - we already have that. We're ONLY asking for visual design. Please just make the content we have look good. You may move parts of the content around a small amount but the functionality is very much signed off now so it's only visual styling that we need addressed.

Please base the branding around the current logo, which can't be changed. You can get the logo as an EPS here : http://clients.brambleotter.co.uk/shiftwellhub/design/logo-green.eps

Here is a link to the current design for the website, and for the application dashboard:
http://clients.brambleotter.co.uk/shiftwellhub/design/

Also, here is a video we've had made which might help you with the brand:
http://clipvaultnet.com/83051726

Just in case it isn't clear, the video (linked in the main brief) is an essential part of the website homepage.

Reason: We need to spend some time looking over these designs and might ask for a few amendments to one or two in the next few days. Thanks.

Target Market(s)

Doctors and medical practices

Industry/Entity Type

Medical

Requirements
Must have
• It must have all the features that are in the linked designs - homepage and dashboard.

```html
<!DOCTYPE html>
<html lang="en">
<head>
<meta charset="utf-8">
<title>Shiftwell Hub – Dashboard</title>
<link rel="stylesheet" href="https://fonts.googleapis.com/css2?family=Lato:wght@400;700&display=swap">
<style>
:root{
  --blue:#1ea6df;
  --blue-dark:#0e8fcf;
  --blue-nav:#29b4ea;
  --title:#6aa2bf;
  --text:#555c63;
  --text-dark:#3b4249;
  --value:#1e9bd7;
  --line:#dfe2e6;
  --panel-head:#eef0f4;
  --orange:#f39a2b;
  --orange-dark:#e5781d;
  --red:#d3232a;
  --green:#7cc242;
  --green-text:#7ab83b;
  --page:#ffffff;
}
*{box-sizing:border-box;margin:0;padding:0}
html,body{width:1200px;height:1116px;overflow:hidden}
body{font-family:"Lato",Arial,sans-serif;color:var(--text);background:var(--page);position:relative;font-size:13px}

.sidebar{position:absolute;left:0;top:0;width:218px;height:1116px;background:#fff;box-shadow:2px 0 6px rgba(0,0,0,.12);z-index:2}
.brand{height:83px;display:flex;align-items:center;padding-left:22px;gap:10px}
.brand-mark{width:34px;height:34px;border-radius:50%;background:var(--blue)}
.brand-name{font-size:21px;font-weight:700;color:var(--blue);letter-spacing:.3px}
.nav a{display:flex;justify-content:space-between;align-items:center;height:41px;padding:0 24px 0 22px;background:var(--blue-nav);color:#fff;text-decoration:none;font-size:15px;border-bottom:1px solid #1b9fd8;position:relative}
.nav a.active{background:var(--blue-dark)}
.nav a.active::after{content:"";position:absolute;right:-10px;top:10px;border:10px solid transparent;border-left-color:var(--blue-dark);border-right:0}
.nav .chev{font-size:14px;opacity:.8}
.badge{display:inline-flex;width:19px;height:19px;border-radius:50%;background:var(--red);font-size:11px;align-items:center;justify-content:center;margin-right:12px}
.nav .right{display:flex;align-items:center}

.topbar{position:absolute;left:218px;top:0;right:0;height:43px;background:linear-gradient(#fafbfd,#e9edf3);border-bottom:1px solid #d6dbe2;display:flex;align-items:center;justify-content:space-between;padding:0 28px 0 28px}
.user{color:#2a8fc4;font-weight:700;font-size:14px;text-transform:uppercase}
.toplinks{display:flex;gap:50px}
.toplinks a{color:#2a8fc4;font-size:11px;text-transform:uppercase;text-decoration:none;letter-spacing:.3px}

.page-title{position:absolute;left:242px;top:62px;font-size:31px;font-weight:400;color:var(--title)}
.cta{position:absolute;left:954px;top:57px;width:209px;height:39px;border-radius:3px;background:linear-gradient(var(--orange),var(--orange-dark));color:#fff;font-size:16px;text-transform:uppercase;display:flex;align-items:center;justify-content:center;box-shadow:0 1px 2px rgba(0,0,0,.25)}

.panel{position:absolute;background:#fbfbfc;border:1px solid var(--line);box-shadow:0 2px 0 #e6e8eb}
.panel-head{height:44px;background:linear-gradient(#f8f9fb,var(--panel-head));border-bottom:1px solid var(--line);display:flex;align-items:center;padding:0 16px;font-size:16px;color:#5b636b;text-transform:uppercase;gap:10px}
.panel-head.plain{text-transform:none;font-size:15px}

.jobs-map{left:239px;top:114px;width:568px;height:483px;background:#f0f1f3}
.map{position:absolute;left:6px;top:55px;width:553px;height:322px;background:linear-gradient(135deg,#e7e4da,#d9e8c9 45%,#e9e5dc 75%,#b9cfe3)}
.map-list{position:absolute;left:6px;top:388px;width:553px}
.map-row{display:grid;grid-template-columns:210px 198px 1fr;height:42px;border:1px solid var(--line);background:linear-gradient(#fff,#f1f2f4);margin-bottom:-1px}
.map-row>div{display:flex;align-items:center;border-right:1px solid var(--line);font-size:13px;justify-content:center}
.map-row>div:first-child{justify-content:flex-start;padding-left:10px;gap:12px}
.pin{width:14px;height:20px}

.table-panel .row{display:flex;justify-content:space-between;align-items:center;height:35px;border-bottom:1px solid var(--line);padding:0 16px;font-size:13px;background:linear-gradient(#fff,#f6f7f8)}
.row .val{color:var(--value);font-weight:700}
.row.highlight{background:#eefaf0}
.my-jobs{left:239px;top:624px;width:270px;height:217px}
.finance{left:537px;top:624px;width:269px;height:251px}
.tabs{display:grid;grid-template-columns:1fr 1fr;height:33px;border-bottom:1px solid var(--line)}
.tab{display:flex;align-items:center;justify-content:center;gap:8px;font-size:12px;background:linear-gradient(#f6f7f9,#e7eaee)}
.tab+.tab{border-left:1px solid var(--line)}
.radio{width:10px;height:10px;border-radius:50%;border:2px solid #9aa3ad}
.radio.on{border-color:#3b7fc0;background:#3b7fc0;box-shadow:inset 0 0 0 2px #fff}

.notifications{left:837px;top:114px;width:326px;height:187px}
.notes{list-style:none;padding:14px 16px}
.notes li{font-size:13px;padding:8px 0 8px 16px;position:relative}
.notes li::before{content:"";position:absolute;left:2px;top:13px;border:4px solid transparent;border-left:6px solid var(--red);border-right:0}
.alert{width:20px;height:20px;border-radius:50%;background:var(--red);color:#fff;font-size:13px;font-weight:700;display:flex;align-items:center;justify-content:center}

.diary{left:837px;top:319px;width:326px;height:297px}
.month{display:flex;justify-content:space-between;align-items:center;padding:6px 8px;height:42px}
.month span{font-size:16px;color:#5b636b}
.arrow{width:22px;height:22px;border:1px solid #c9d1da;background:#fff;display:flex;align-items:center;justify-content:center}
.cal{display:grid;grid-template-columns:repeat(7,44px);gap:1px;margin:0 0 0 6px}
.cal .dow{font-size:11px;text-align:center;padding:6px 0 8px}
.d{height:23px;font-size:11px;color:#fff;display:flex;align-items:center;justify-content:center}
.d.r{background:var(--red)}.d.g{background:var(--green)}.d.o{background:var(--orange)}.d.e{background:#e9ebee}
.legend{display:flex;gap:16px;padding:14px 10px 4px;font-size:11px}
.legend i{display:inline-block;width:14px;height:10px;margin-right:6px;vertical-align:-1px}
.see-all{font-size:11px;color:var(--value);padding:2px 10px}

.job-card{left:837px;top:635px;width:326px}
.job-card.next{top:865px}
.job-body{display:flex;justify-content:space-between;padding:14px 16px;height:111px}
.job-name{font-weight:700;font-size:14px;color:var(--text-dark);margin-bottom:6px}
.addr{font-size:13px;line-height:18px}
.when{color:var(--value);font-size:13px;line-height:16px;width:150px}
.job-foot{background:linear-gradient(#e6ebf2,#f4f6f9);padding:8px 16px;font-size:12px;line-height:18px;height:54px}
.job-foot b{color:var(--green-text);font-weight:400}
.job-foot .star{color:var(--green-text)}
</style>
</head>
<body>

<aside class="sidebar">
  <div class="brand"><span class="brand-mark"></span><span class="brand-name">Shiftwell Hub</span></div>
  <nav class="nav">
    <a class="active" href="#">Dashboard<span class="right"><span class="badge">2</span><span class="chev">›</span></span></a>
    <a href="#">Profile<span class="chev">›</span></a>
    <a href="#">My Jobs<span class="chev">›</span></a>
    <a href="#">My Finances<span class="chev">›</span></a>
    <a href="#">My Network<span class="chev">›</span></a>
  </nav>
</aside>

<header class="topbar">
  <span class="user">Mrs Helen Marlow</span>
  <nav class="toplinks"><a href="#">Profile</a><a href="#">Settings</a><a href="#">Referal</a><a href="#">Signout</a></nav>
</header>

<h1 class="page-title">Dashboard</h1>
<div class="cta">Get Started</div>

<section class="panel jobs-map">
  <div class="panel-head plain">Jobs within 20 miles</div>
  <div class="map" role="img" aria-label="Street map of the surrounding area with pins marking nearby surgeries"></div>
  <div class="map-list">
    <div class="map-row">
      <div><svg class="pin" viewBox="0 0 14 20"><path d="M7 0a7 7 0 0 1 7 7c0 5-7 13-7 13S0 12 0 7a7 7 0 0 1 7-7z" fill="#f27a6b"/><text x="7" y="10" font-size="7" fill="#fff" text-anchor="middle" font-family="Lato,sans-serif">A</text></svg>Willow Lane Surgery</div>
      <div>14 Jobs Available</div><div>0.8 miles</div>
    </div>
    <div class="map-row">
      <div><svg class="pin" viewBox="0 0 14 20"><path d="M7 0a7 7 0 0 1 7 7c0 5-7 13-7 13S0 12 0 7a7 7 0 0 1 7-7z" fill="#f27a6b"/><text x="7" y="10" font-size="7" fill="#fff" text-anchor="middle" font-family="Lato,sans-serif">B</text></svg>Mill Street Surgery</div>
      <div>0 Jobs Available</div><div>2.73 miles</div>
    </div>
  </div>
</section>

<section class="panel table-panel my-jobs">
  <div class="panel-head">My Jobs</div>
  <div class="row"><span>Jobs Booked</span><span class="val">17</span></div>
  <div class="row"><span>Jobs Requiring Confirmation</span><span class="val">0</span></div>
  <div class="row"><span>Pending Applications</span><span class="val">2</span></div>
  <div class="row"><span>Jobs Invited</span><span class="val">1</span></div>
  <div class="row"><span>My Network</span><span class="val">9</span></div>
</section>

<section class="panel table-panel finance">
  <div class="panel-head">Financial Summary</div>
  <div class="tabs"><div class="tab"><span class="radio on"></span>Tax Year</div><div class="tab"><span class="radio"></span>Current Tax</div></div>
  <div class="row"><span>Paid Invoices</span><span class="val">£53,769</span></div>
  <div class="row"><span>Unpaid Invoices</span><span class="val">£3,188</span></div>
  <div class="row highlight"><span>Total Earned</span><span class="val">£56,957</span></div>
  <div class="row"><span>Pension Claimed</span><span class="val">£5,238</span></div>
  <div class="row"><span>Expenses</span><span class="val">£2,413</span></div>
</section>

<section class="panel notifications">
  <div class="panel-head"><span class="alert">!</span>Notifications</div>
  <ul class="notes">
    <li>Mill Street Surgery has posted a new job.</li>
    <li>Mill Street Surgery has posted a new job.</li>
    <li>Mill Street Surgery has posted a new job.</li>
  </ul>
</section>

<section class="panel diary">
  <div class="panel-head">My Diary</div>
  <div class="month">
    <span class="arrow"><svg width="8" height="10" viewBox="0 0 8 10"><path d="M7 0 0 5l7 5z" fill="#1e9bd7"/></svg></span>
    <span>January 2013</span>
    <span class="arrow"><svg width="8" height="10" viewBox="0 0 8 10"><path d="M1 0l7 5-7 5z" fill="#1e9bd7"/></svg></span>
  </div>
  <div class="cal">
    <div class="dow">Sun</div><div class="dow">Mon</div><div class="dow">Tue</div><div class="dow">Wed</div><div class="dow">Thu</div><div class="dow">Fri</div><div class="dow">Sat</div>
    <div class="d e"></div><div class="d r">1</div><div class="d g">2</div><div class="d o">3</div><div class="d o">4</div><div class="d o">5</div><div class="d g">6</div>
    <div class="d r">7</div><div class="d r">8</div><div class="d g">9</div><div class="d g">10</div><div class="d g">11</div><div class="d o">12</div><div class="d g">13</div>
    <div class="d g">14</div><div class="d g">15</div><div class="d g">16</div><div class="d r">17</div><div class="d r">18</div><div class="d g">19</div><div class="d g">20</div>
    <div class="d g">21</div><div class="d g">22</div><div class="d g">23</div><div class="d o">24</div><div class="d o">25</div><div class="d g">26</div><div class="d g">27</div>
    <div class="d r">28</div><div class="d r">29</div><div class="d g">30</div><div class="d g">31</div><div class="d e"></div><div class="d e"></div><div class="d e"></div>
  </div>
  <div class="legend">
    <span><i style="background:var(--red)"></i>Busy</span>
    <span><i style="background:var(--orange)"></i>Partially available</span>
    <span><i style="background:var(--green)"></i>Available</span>
  </div>
  <div class="see-all">See all appointments</div>
</section>

<section class="panel job-card">
  <div class="panel-head">Current or Next Job</div>
  <div class="job-body">
    <div><div class="job-name">Ashgrove Surgery</div><div class="addr">24 Elm Parade<br>London<br>N9 2QX</div></div>
    <div class="when">17 Jan 2012 - 24 Jan 2013 (09.30 - 16.00)</div>
  </div>
  <div class="job-foot"><span class="star">*</span> Earnings from this employer: <b>£23,887</b><br><span class="star">*</span> This surgery has <b>8</b> unfilled jobs</div>
</section>

<section class="panel job-card next">
  <div class="panel-head">Following</div>
  <div class="job-body">
    <div><div class="job-name">Dr Okafor Surgery</div><div class="addr">24 Elm Parade<br>London<br>N9 2QX</div></div>
    <div class="when">23 Jan 2012 (09.30 - 15.30)</div>
  </div>
  <div class="job-foot"><span class="star">*</span> Earnings from this employer: <b>£6,523</b><br><span class="star">*</span> This surgery has no unfilled jobs</div>
</section>

</body>
</html>
```